Relocation/furniture installation company needs new business cards

we are a relocation and furniture installation company mainly dealing with corporate clients and we are looking for new business card ideas. Cards should incorporate our logo and list our website, phone number and services. The company is only 2 years old but with more staff joining we are in the need for more business cards, so something with an awesome design that is eye catching would go a long way to insure we get our name out there and look good to potential new clients.

Target Market(s)

Corporate

Industry/Entity Type

Trade

Contact Information for Business Card

www.mervoline.co.nz
0508 4 bravok

furniture installation
business relocations
joinery installation
commercial property maintenance

Colors
0592cd
34a7d8
85cae6
85acd3
0356a4
cfdfed
cee9f5
757575
474747

Requirements
Must have
• Business relocations and furniture installation specialists
Nice to have
• something that incorporates our logo.

```html
<!DOCTYPE html>
<html lang="en">
<head>
<meta charset="utf-8">
<title>Mervoline Business Card</title>
<link rel="stylesheet" href="https://fonts.googleapis.com/css2?family=Source+Sans+3:wght@400;600&display=swap">
<style>
  :root {
    --stage: #353535;
    --card-light: #ebeaeb;
    --navy: #2a3b8f;
    --cyan: #1ab0e6;
    --white: #ffffff;
    --blue-deep: #1f67b3;
    --blue-bright: #00aeef;
  }
  * { margin: 0; padding: 0; box-sizing: border-box; }
  html, body {
    width: 1200px; height: 900px; overflow: hidden;
    background: var(--stage);
    font-family: "Source Sans 3", "Myriad Pro", Arial, sans-serif;
  }
  .card {
    position: absolute; top: 306px;
    width: 440px; height: 271px;
    border-radius: 10px; overflow: hidden;
    box-shadow: 2px 3px 6px rgba(0,0,0,0.45);
  }
  .card-front { left: 149px; background: var(--card-light); }
  .card-back {
    left: 608px;
    background: radial-gradient(ellipse 75% 85% at 62% 38%, var(--blue-bright) 0%, #0aa3e4 40%, var(--blue-deep) 100%);
  }
  .brand-name {
    position: absolute; left: 0; right: 0;
    text-align: center;
    color: var(--navy);
    font-weight: 600;
    letter-spacing: 3px;
  }
  .card-front .brand-name { top: 90px; font-size: 40px; line-height: 44px; }
  .card-back .brand-name { top: 150px; font-size: 40px; line-height: 44px; }
  .contact-band {
    position: absolute; left: 0; right: 0; top: 145px; height: 46px;
    background: var(--navy);
    display: flex; align-items: center; justify-content: center; gap: 18px;
    color: var(--white); font-size: 16px;
  }
  .contact-item { display: flex; align-items: center; gap: 6px; }
  .contact-item svg { width: 15px; height: 15px; fill: var(--white); }
  .services {
    position: absolute; left: 0; right: 0; top: 207px;
    color: var(--navy); font-size: 14px; text-align: center; line-height: 26px;
  }
  .service { white-space: nowrap; }
  .service::before {
    content: ""; display: inline-block;
    width: 6px; height: 6px; border-radius: 50%;
    background: var(--cyan);
    margin: 0 4px 2px 4px; vertical-align: middle;
  }
</style>
</head>
<body>
  <section class="card card-front">
    <div class="brand-name">MERVOLINE</div>
    <div class="contact-band">
      <span class="contact-item">
        <svg viewBox="0 0 24 24" aria-hidden="true"><path d="M6.6 10.8a15.1 15.1 0 0 0 6.6 6.6l2.2-2.2c.3-.3.7-.4 1-.2 1.1.4 2.3.6 3.6.6.6 0 1 .4 1 1V20c0 .6-.4 1-1 1C10.6 21 3 13.4 3 4c0-.6.4-1 1-1h3.5c.6 0 1 .4 1 1 0 1.2.2 2.4.6 3.6.1.3 0 .7-.2 1z"/></svg>
        0508 4 bravok
      </span>
      <span class="contact-item">
        <svg viewBox="0 0 24 24" aria-hidden="true"><path d="M12 2a10 10 0 1 0 0 20 10 10 0 0 0 0-20zm-1 17.9A8 8 0 0 1 4.1 10.6L9 15.5v1a2 2 0 0 0 2 2zm6.9-2.5A2 2 0 0 0 16 16h-1v-3a1 1 0 0 0-1-1H8v-2h2a1 1 0 0 0 1-1V7h2a2 2 0 0 0 2-2v-.4a8 8 0 0 1 2.9 12.8z"/></svg>
        www.mervoline.co.nz
      </span>
    </div>
    <div class="services">
      <div><span class="service">Furniture Installation</span> <span class="service">Business Relocations</span></div>
      <div><span class="service">Joinery Installation</span> <span class="service">Commercial Property Maintenance</span></div>
    </div>
  </section>
  <section class="card card-back">
    <div class="brand-name">MERVOLINE</div>
  </section>
</body>
</html>
```